Poly Gel bottle Design that stands out for Nail Company

I need a label design for the poly gel polish bottle. We are looking for a design that fit our brand store color and a clean design similar to our competitor.

We have 3 bottle Title: Gel Top Coat, Gel base Coat, Gel Matte Coat
The bottle will be white.

Also I will need 1 label for the extension gel.

Bottle volume is 15ml/0.5 fl oz

Target Market(s)

beauty acrylic nail and poly gel nail

Industry/Entity Type

Nail

Font styles to use
Serif
Decorative

Colors
6c459b

Requirements
Must have
• store color scheme. www.tealpebbleshop.com

```html
<!DOCTYPE html>
<html lang="en">
<head>
<meta charset="utf-8">
<title>Teal Pebble – Gel Top Coat Labels</title>
<link rel="stylesheet" href="https://fonts.googleapis.com/css2?family=Josefin+Sans:wght@400;600&family=Arimo:wght@400&display=swap">
<style>
  :root {
    --backdrop: #f8e5f0;
    --fuchsia: #e91e8c;
    --fuchsia-deep: #b0106e;
    --fuchsia-pale: #eca6d2;
    --magenta: #c8168a;
    --plum: #7a1f80;
    --violet: #6c459b;
    --violet-deep: #553a86;
    --orchid: #d98ab8;
    --mauve: #9a5c9a;
    --lavender: #e6dff0;
    --ink: #000000;
    --paper: #ffffff;
  }
  html, body {
    margin: 0;
    padding: 0;
    width: 1200px;
    height: 838px;
    overflow: hidden;
    background: var(--backdrop);
  }
  .label-range {
    position: relative;
    width: 1200px;
    height: 838px;
  }
  .label {
    position: absolute;
    top: 376px;
    width: 240px;
    height: 288px;
    border-radius: 14px 14px 10px 10px;
    box-shadow: 0 10px 18px -8px rgba(60, 40, 60, 0.45);
    font-family: "Josefin Sans", sans-serif;
    text-align: center;
  }
  .label--fuchsia {
    left: 147px;
    background: linear-gradient(180deg, var(--fuchsia) 0%, #d0157e 45%, var(--fuchsia-deep) 80%, var(--fuchsia-pale) 100%);
  }
  .label--plum {
    left: 470px;
    background: linear-gradient(180deg, #b80c7c 0%, #9c0f72 30%, var(--plum) 55%, var(--violet-deep) 85%, #c8c0e6 100%);
  }
  .label--orchid {
    left: 789px;
    background: linear-gradient(180deg, var(--orchid) 0%, #b67aa8 30%, var(--mauve) 50%, var(--violet) 80%, var(--violet-deep) 100%);
  }
  .brand-name {
    position: absolute;
    top: 86px;
    left: 0;
    right: 0;
    margin: 0;
    font-weight: 600;
    font-size: 31px;
    letter-spacing: 0.5px;
    line-height: 1;
  }
  .product-title {
    position: absolute;
    top: 147px;
    left: 38px;
    width: 164px;
    height: 24px;
    margin: 0;
    font-weight: 400;
    font-size: 19px;
    line-height: 27px;
    letter-spacing: 0.3px;
  }
  .product-type {
    position: absolute;
    top: 173px;
    left: 0;
    right: 0;
    margin: 0;
    font-family: "Arimo", sans-serif;
    font-size: 11px;
  }
  .product-volume {
    position: absolute;
    top: 223px;
    left: 0;
    right: 0;
    margin: 0;
    font-size: 10px;
  }
  .label--fuchsia .brand-name { color: var(--ink); }
  .label--fuchsia .product-title { background: var(--ink); color: var(--fuchsia); }
  .label--fuchsia .product-type,
  .label--fuchsia .product-volume { color: var(--ink); }

  .label--plum .brand-name { color: var(--magenta); }
  .label--plum .product-title { background: var(--magenta); color: var(--ink); }
  .label--plum .product-type { color: var(--magenta); top: 181px; }
  .label--plum .product-volume { color: var(--ink); }

  .label--orchid .brand-name { color: var(--paper); }
  .label--orchid .product-title { background: var(--lavender); color: var(--violet); }
  .label--orchid .product-type { color: var(--paper); top: 179px; }
  .label--orchid .product-volume { color: var(--paper); }
</style>
</head>
<body>
  <main class="label-range">
    <section class="label label--fuchsia">
      <h2 class="brand-name">teal pebble</h2>
      <p class="product-title">GEL TOP COAT</p>
      <p class="product-type">poly gel polish</p>
      <p class="product-volume">15ml/0.5 fl oz</p>
    </section>
    <section class="label label--plum">
      <h2 class="brand-name">teal pebble</h2>
      <p class="product-title">GEL TOP COAT</p>
      <p class="product-type">poly gel polish</p>
      <p class="product-volume">15ml/0.5 fl oz</p>
    </section>
    <section class="label label--orchid">
      <h2 class="brand-name">teal pebble</h2>
      <p class="product-title">GEL TOP COAT</p>
      <p class="product-type">poly gel polish</p>
      <p class="product-volume">15ml/0.5 fl oz</p>
    </section>
  </main>
</body>
</html>
```